Etiketten für Olivenöl
Zielgruppe
Handel mit Oliven und Olivenölen unsere Zielgruppe sind qualitativ anspruchsvolle Menschen.
Aufgabenstellung
Wir benötigen ein Produktetikett für eine Olivenöl Flasche Form Malvena 250ml und 500ml mit Vorder- und Rückseite Lg. 14cm und Br. 5cm für 250 ml Flasche und Lg. 18cm und Br. 7cm für 500ml Flasche.
Das Etikett kann gern einen matten Hintergrund haben oder auch ganz durchsichtig sein.
Der Name Verunta bedeutet Olivenbaum und sollte berücksichtigt werden.
Folgende Angaben bzw. Felder muss das Etikett beinhalten:
Barcode, Inhaltsstoffe, Haltbarkeitsdatum, Artikelnummer

```html
<!DOCTYPE html>
<html lang="de">
<head>
<meta charset="utf-8">
<title>Verunta – Olivenöl Etiketten</title>
<link rel="stylesheet" href="https://fonts.googleapis.com/css2?family=Gilda+Display&family=Jost:wght@300;400;500;600&family=Barlow+Condensed:wght@300;400;500&display=swap">
<style>
  :root {
    --page-bg: #f4f4f4;
    --label-bg: #3a393b;
    --copper: #e3a66c;
    --copper-soft: rgba(227, 166, 108, 0.14);
    --copper-faint: rgba(227, 166, 108, 0.03);
    --white: #ffffff;
    --ink: #1c1c1c;
  }
  * { margin: 0; padding: 0; box-sizing: border-box; }
  html, body { width: 1200px; height: 2779px; overflow: hidden; background: var(--page-bg); }
  .canvas { position: relative; width: 1200px; height: 2779px; }

  .label {
    position: absolute;
    width: 512px; height: 1432px;
    background: var(--label-bg);
    color: var(--copper);
    overflow: hidden;
    transform-origin: top left;
  }
  .label > * { position: absolute; left: 0; right: 0; text-align: center; }

  .branch-art {
    background: linear-gradient(180deg, var(--copper-faint) 0%, var(--copper-soft) 55%, var(--copper-faint) 100%);
  }

  .brand-mark {
    left: 50%; right: auto; width: 110px; height: 110px; margin-left: -55px;
    top: 164px; border: 3px solid var(--copper); border-radius: 50%;
  }
  .brand-name {
    top: 297px;
    font-family: "Gilda Display", serif; font-size: 20px; line-height: 24px; letter-spacing: 5px;
  }

  .caps {
    font-family: "Jost", sans-serif; font-weight: 500;
    font-size: 30px; letter-spacing: 7px; line-height: 39px;
  }
  .grade { top: 410px; }
  .quality { top: 790px; }
  .title { font-family: "Gilda Display", serif; font-weight: 400; line-height: 1; }
  .title-oliven { top: 494px; font-size: 125px; }
  .title-oel { top: 624px; font-size: 155px; }
  .volume {
    top: 1260px;
    font-family: "Jost", sans-serif; font-weight: 500; font-size: 31px; line-height: 36px; letter-spacing: 8px;
  }
  .front .branch-art { top: 880px; bottom: 0; }

  .info {
    font-family: "Jost", sans-serif; font-weight: 300;
    font-size: 21px; letter-spacing: 2px; line-height: 27px;
  }
  .ingredients { top: 391px; }
  .storage { top: 466px; }
  .address { top: 998px; }
  .best-before { top: 1140px; }

  .nutrition {
    left: 94px; right: auto; width: 337px; top: 554px; height: 383px;
    border: 2px solid var(--copper); text-align: left;
    padding: 8px 20px;
    font-family: "Barlow Condensed", sans-serif; font-weight: 300; font-size: 24px; line-height: 33px;
  }
  .nutrition h3 { font-weight: 400; font-size: 24px; }
  .nutrition .row { display: flex; justify-content: space-between; }
  .nutrition .group { margin-top: 31px; }

  .back .branch-left { left: 0; right: auto; width: 100px; top: 880px; bottom: 0; }
  .back .branch-right { left: auto; right: 0; width: 90px; top: 940px; bottom: 0; }
  .barcode-field {
    left: 75px; right: auto; width: 373px; top: 1271px; height: 161px;
    background: var(--white); color: var(--ink);
    font-family: "Jost", sans-serif; font-weight: 600; font-size: 25px;
    padding-top: 43px;
  }

  .top-front { left: 70px; top: 67px; }
  .top-back { left: 628px; top: 67px; }
  .mini-front { left: 91px; top: 1998px; transform: scale(0.41); }
  .mini-back { left: 414px; top: 1998px; transform: scale(0.41); }
  .large-front { left: 837px; top: 1865px; transform: scale(0.47); }
</style>
</head>
<body>
<main class="canvas">

  <section class="label front top-front">
    <div class="branch-art" role="img" aria-label="Linienzeichnung von Olivenzweigen mit Früchten"></div>
    <div class="brand-mark"></div>
    <p class="brand-name">VERUNTA</p>
    <p class="caps grade">EXTRA<br>NATIVES</p>
    <h1 class="title title-oliven">Oliven</h1>
    <h1 class="title title-oel">Öl</h1>
    <p class="caps quality">PREMIUM<br>QUALITY</p>
    <p class="volume">250ml</p>
  </section>

  <section class="label back top-back">
    <div class="branch-art branch-left" role="img" aria-label="Olivenzweig-Zeichnung am linken Rand"></div>
    <div class="branch-art branch-right" role="img" aria-label="Olivenzweig-Zeichnung am rechten Rand"></div>
    <div class="brand-mark"></div>
    <p class="brand-name">VERUNTA</p>
    <p class="info ingredients">ZUTATEN:<br>100% NATIVES OLIVENÖL</p>
    <p class="info storage">VOR WÄRME UND LICHT<br>GESCHÜTZT LAGERN.</p>
    <div class="nutrition">
      <h3>Nährwertangabe pro 100ml</h3>
      <div class="row"><span>Energie</span><span>25,6 kcal / 107,4 KJ</span></div>
      <div class="group">
        <div class="row"><span>Fett</span><span>0,0 g</span></div>
        <div class="row"><span>davon ges. Fettsäuren</span><span>0,0 g</span></div>
      </div>
      <div class="group">
        <div class="row"><span>Kohlenhydrate</span><span>6,2 g</span></div>
        <div class="row"><span>davon Zucker</span><span>6,2 g</span></div>
      </div>
      <div class="group">
        <div class="row"><span>Eiweiss</span><span>0,1 g</span></div>
        <div class="row"><span>Salz</span><span>0,0 g</span></div>
      </div>
    </div>
    <p class="info address">VERUNTA<br>MUSTERSTR. 11<br>12345 MUSTERSTADT<br>WWW.VERUNTA.DE</p>
    <p class="info best-before">UNGEÖFFNET MINDESTENS<br>HALTBAR BIS:</p>
    <div class="barcode-field">BARCODE</div>
  </section>

  <section class="label front mini-front">
    <div class="branch-art" role="img" aria-label="Linienzeichnung von Olivenzweigen mit Früchten"></div>
    <div class="brand-mark"></div>
    <p class="brand-name">VERUNTA</p>
    <p class="caps grade">EXTRA<br>NATIVES</p>
    <h2 class="title title-oliven">Oliven</h2>
    <h2 class="title title-oel">Öl</h2>
    <p class="caps quality">PREMIUM<br>QUALITY</p>
    <p class="volume">250ml</p>
  </section>

  <section class="label back mini-back">
    <div class="branch-art branch-left" role="img" aria-label="Olivenzweig-Zeichnung am linken Rand"></div>
    <div class="branch-art branch-right" role="img" aria-label="Olivenzweig-Zeichnung am rechten Rand"></div>
    <div class="brand-mark"></div>
    <p class="brand-name">VERUNTA</p>
    <p class="info ingredients">ZUTATEN:<br>100% NATIVES OLIVENÖL</p>
    <p class="info storage">VOR WÄRME UND LICHT<br>GESCHÜTZT LAGERN.</p>
    <div class="nutrition">
      <h3>Nährwertangabe pro 100ml</h3>
      <div class="row"><span>Energie</span><span>25,6 kcal / 107,4 KJ</span></div>
      <div class="group">
        <div class="row"><span>Fett</span><span>0,0 g</span></div>
        <div class="row"><span>davon ges. Fettsäuren</span><span>0,0 g</span></div>
      </div>
      <div class="group">
        <div class="row"><span>Kohlenhydrate</span><span>6,2 g</span></div>
        <div class="row"><span>davon Zucker</span><span>6,2 g</span></div>
      </div>
      <div class="group">
        <div class="row"><span>Eiweiss</span><span>0,1 g</span></div>
        <div class="row"><span>Salz</span><span>0,0 g</span></div>
      </div>
    </div>
    <p class="info address">VERUNTA<br>MUSTERSTR. 11<br>12345 MUSTERSTADT<br>WWW.VERUNTA.DE</p>
    <p class="info best-before">UNGEÖFFNET MINDESTENS<br>HALTBAR BIS:</p>
    <div class="barcode-field">BARCODE</div>
  </section>

  <section class="label front large-front">
    <div class="branch-art" role="img" aria-label="Linienzeichnung von Olivenzweigen mit Früchten"></div>
    <div class="brand-mark"></div>
    <p class="brand-name">VERUNTA</p>
    <p class="caps grade">EXTRA<br>NATIVES</p>
    <h2 class="title title-oliven">Oliven</h2>
    <h2 class="title title-oel">Öl</h2>
    <p class="caps quality">PREMIUM<br>QUALITY</p>
    <p class="volume">500ml</p>
  </section>

</main>
</body>
</html>
```